Book cover design for "The Hollowmere", supernatural thriller, (sub)urban fantasy genres

I need a full book cover design for my new novel, "The Hollowmere", Subtitle: "Book 1: Marcus" a story whose heart is about friendships, family, and small towns wrapped in the skin of a supernatural thriller and (sub)urban fantasy. I would like to see designs using those genre elements and colors but also carrying elements of fear and danger. The book would also fall somewhere into into YA and NA categories. I came up with a simple starting point and some other covers conveying some of the elements I like. They are attached.

```html
<!DOCTYPE html>
<html lang="en">
<head>
<meta charset="UTF-8">
<title>The Hollowmere — Book 1: Marcus</title>
<link rel="stylesheet" href="https://fonts.googleapis.com/css2?family=Bodoni+Moda:opsz,wght@6..96,400&family=Parisienne&family=Forum&display=swap">
<style>
  :root {
    --page: #ffffff;
    --cover-red: #7c1b1d;
    --cover-red-deep: #5e1214;
    --forest-teal: #1f6a5c;
    --glow: #efb877;
    --glow-soft: #c98a4e;
    --ground: #3a2418;
    --base-dark: #140c0a;
    --title-cream: #f4eedb;
  }
  * { margin: 0; padding: 0; box-sizing: border-box; }
  html, body {
    width: 1200px;
    height: 1106px;
    overflow: hidden;
    background: var(--page);
  }
  .book-cover {
    position: absolute;
    left: 300px;
    top: 28px;
    width: 600px;
    height: 1050px;
    overflow: hidden;
    background: var(--cover-red);
  }
  .cover-art {
    position: absolute;
    inset: 0;
    background:
      radial-gradient(ellipse 150px 230px at 330px 640px, rgba(255, 214, 150, 0.95), rgba(239, 184, 119, 0.55) 45%, rgba(201, 138, 78, 0) 100%),
      radial-gradient(ellipse 60px 45px at 250px 860px, rgba(40, 150, 130, 0.85), rgba(31, 106, 92, 0) 100%),
      radial-gradient(ellipse 120px 260px at 40px 560px, rgba(31, 106, 92, 0.75), rgba(31, 106, 92, 0) 100%),
      radial-gradient(ellipse 110px 240px at 590px 620px, rgba(31, 106, 92, 0.45), rgba(31, 106, 92, 0) 100%),
      linear-gradient(to bottom,
        var(--cover-red-deep) 0%,
        var(--cover-red) 30%,
        #7a3a24 52%,
        var(--glow-soft) 64%,
        var(--ground) 77%,
        #241612 84%,
        var(--base-dark) 100%);
  }
  .cover-title {
    position: absolute;
    left: 0;
    right: 0;
    top: 0;
    font-weight: 400;
    color: var(--title-cream);
  }
  .title-article {
    position: absolute;
    left: 112px;
    top: 70px;
    font-family: "Parisienne", cursive;
    font-size: 88px;
    line-height: 1;
    white-space: nowrap;
  }
  .title-main {
    position: absolute;
    left: 40px;
    right: 40px;
    top: 232px;
    text-align: center;
    font-family: "Bodoni Moda", serif;
    font-weight: 400;
    font-size: 90px;
    line-height: 1;
    letter-spacing: 0;
    white-space: nowrap;
  }
  .series-line {
    position: absolute;
    right: 78px;
    top: 342px;
    font-family: "Parisienne", cursive;
    font-size: 34px;
    line-height: 1;
    white-space: nowrap;
    color: var(--title-cream);
  }
  .author-name {
    position: absolute;
    left: 0;
    right: 0;
    top: 968px;
    text-align: center;
    font-family: "Forum", serif;
    font-size: 42px;
    line-height: 1;
    letter-spacing: 1px;
    white-space: nowrap;
    color: var(--title-cream);
  }
</style>
</head>
<body>
  <div class="book-cover">
    <div class="cover-art" role="img" aria-label="Cover photograph: a tunnel of twisted trees in a red-tinted forest opening onto a glowing golden light, with four silhouetted young men standing on a dirt path above a puddle reflecting teal light"></div>
    <h1 class="cover-title">
      <span class="title-article">The</span>
      <span class="title-main">hollowmere</span>
    </h1>
    <p class="series-line">Book 1: Marcus</p>
    <p class="author-name">JULIAN CASTOVER</p>
  </div>
</body>
</html>
```